Progressive European Honey Business needs minimalistic packaging design

Hello - thank you for your interest in our brief. We are Velvet Jinx, a London based Honey business, importing only the best honey Europe has to offer. Our values are deeply rooted with in progressive liberal values and we are looking for minimalist packaging, which reflects that.

We are looking for a design, which dimensions fit with our packaging option (Kelmor Glass Jar | HEIGHT 90mm | DIAMETER 63mm). We will require a various output files (High Resolution JPEG (CMYK Colors 300 dpi) Source File Ai, PSD, PDF, Printing files (die cut, die folding) and a 3D Mockup of the packaging for use within digital commerce platforms.

We must be able to adjust the free text on the label front and it should include the following:
Brand Name
Honey type
Limited edition No. X / 100 ( X being the number of purchase i.e. 25 / 100)
EU Honey, Single Orgin (Germany)
(c) The net weight (250g)

The back must include room for additional information (again adjustable by us) and the following:
“Unsuitable for children under 12 months”
(b) The appropriate durability declaration

In total, we are looking for
a) A front label
b) A back label
c) A seal (round) including the attached bee and logo included in the Zip file.
Do note that a) & b) can also be combined into one design as long as the symmetry on the jar stays intact.

The final design should communicate modern aesthetics, high quality, that are slightly provocative and pop off the shelves.
Updates

Hi folks, sorry for the delay in completing this project, but my business partner had a leak in his house. We planned to finalise our review today, but this will have to wait until it's no longer raining in his livingroom. Our sincere apologies!

Other font styles liked:
• See branding guidelines

Requirements
Must have
• Must follow the branding guideline and fonts provided as attachment

```html
<!DOCTYPE html>
<html lang="en">
<head>
<meta charset="utf-8">
<title>Velvet Jinx – Seal and Front Label</title>
<link rel="stylesheet" href="https://fonts.googleapis.com/css2?family=Rubik+Mono+One&family=Ultra&family=Nanum+Pen+Script&display=swap">
<style>
  :root {
    --bg: #cccccc;
    --honey: #f5c823;
    --honey-light: #fde23a;
    --honey-deep: #d9a90c;
    --white: #ffffff;
    --ink: #1b1b1b;
    --bee-tone: #e9b820;
  }
  * { margin: 0; padding: 0; box-sizing: border-box; }
  html, body { width: 1200px; height: 935px; overflow: hidden; background: var(--bg); }
  .canvas { position: relative; width: 1200px; height: 935px; }

  /* Round seal */
  .seal {
    position: absolute; left: 178px; top: 249px;
    width: 386px; height: 386px; border-radius: 50%;
    overflow: hidden;
    box-shadow: 2px 3px 4px rgba(0,0,0,0.45);
  }
  .seal svg { position: absolute; inset: 0; }
  .seal-mascot {
    position: absolute; left: 118px; top: 54px; width: 150px; height: 214px;
    border-radius: 48% 48% 40% 40%;
    background: radial-gradient(circle at 55% 45%, var(--bee-tone) 0%, #3a3220 70%, #1b1b1b 100%);
    opacity: 0.9;
  }
  .seal-name {
    position: absolute; left: 0; width: 100%; top: 274px; text-align: center;
    font-family: "Rubik Mono One", sans-serif; font-size: 27px; color: var(--ink);
    letter-spacing: -0.5px;
  }

  /* Front label */
  .label { position: absolute; left: 714px; top: 278px; width: 300px; height: 430px; }
  .label svg { position: absolute; inset: 0; }
  .label-brand {
    position: absolute; left: 18px; top: 50px; width: 276px; text-align: center;
    font-family: "Rubik Mono One", sans-serif; font-size: 26px; color: var(--ink);
    letter-spacing: -0.5px;
  }
  .honey-type {
    position: absolute; left: 22px; top: 150px;
    font-family: "Ultra", serif; font-size: 52px; line-height: 58px; color: var(--ink);
  }
  .label-details {
    position: absolute; left: 36px; top: 328px; width: 250px; text-align: center;
    font-family: "Nanum Pen Script", cursive; font-size: 21px; line-height: 19px; color: var(--ink);
  }
  .label-weight { margin-top: 26px; }
</style>
</head>
<body>
<div class="canvas">

  <div class="seal">
    <svg viewBox="0 0 386 386" width="386" height="386" aria-hidden="true">
      <rect width="386" height="386" fill="var(--honey)"/>
      <path d="M386 95 C330 85 300 80 260 100 C235 115 250 150 255 185 C262 230 230 265 170 285 C130 300 120 330 125 386 L386 386 Z" fill="var(--white)"/>
    </svg>
    <div class="seal-mascot" role="img" aria-label="Crowned bee mascot illustration"></div>
    <div class="seal-name">VELVET JINX</div>
  </div>

  <div class="label">
    <svg viewBox="0 0 300 430" width="300" height="430" aria-hidden="true">
      <defs>
        <linearGradient id="labelHoney" x1="0" y1="0" x2="1" y2="0">
          <stop offset="0" stop-color="var(--honey)"/>
          <stop offset="0.7" stop-color="var(--honey-light)"/>
          <stop offset="1" stop-color="var(--honey-deep)"/>
        </linearGradient>
        <clipPath id="labelShape">
          <path d="M40 8 Q40 0 50 0 L250 0 Q260 0 260 8 L260 14 Q260 20 270 20 L292 20 Q300 20 300 30 L300 395 Q300 405 290 405 L285 405 Q280 405 280 415 L280 422 Q280 430 270 430 L30 430 Q20 430 20 422 L20 415 Q20 405 12 405 L8 405 Q0 405 0 395 L0 30 Q0 20 10 20 L30 20 Q40 20 40 14 Z"/>
        </clipPath>
      </defs>
      <g clip-path="url(#labelShape)">
        <rect width="300" height="430" fill="url(#labelHoney)"/>
        <path d="M300 95 C270 90 230 100 210 120 C185 140 200 170 195 200 C190 240 140 250 110 280 C90 300 85 330 20 350 L0 360 L0 430 L300 430 Z" fill="var(--white)"/>
        <path d="M97 278 C92 290 84 298 84 305 C84 313 90 318 97 318 C104 318 110 313 110 305 C110 298 102 290 97 278 Z" fill="var(--honey)"/>
        <ellipse cx="252" cy="186" rx="7" ry="13" fill="var(--honey-deep)"/>
      </g>
    </svg>
    <div class="label-brand">VELVET JINX</div>
    <div class="honey-type">Raw<br>Honey</div>
    <div class="label-details">
      <p>Limited edition No. 12/100</p>
      <p>EU Honey, Single Orgin (Germany)</p>
      <p class="label-weight">Net weight (250g)</p>
    </div>
  </div>

</div>
</body>
</html>
```